mapleridgegroup Business Card Design

Business card with logo design for mapleridgegroup. We are a group of professional project managers based on the Pareto Principle that 80% of the work is done by 20% of the people. I have a makeshift logo that uses a pi chart with 30% and 20% and the 20% pie slice is set slightly out and up. Have played around with a teal and orange colour scheme.

Industry/Entity Type

Business

Contact Information for Business Card

Gareth Pembroke
Director
mapleridgegroup

0452 803716

```html
<!DOCTYPE html>
<html lang="en">
<head>
<meta charset="utf-8">
<title>mapleridgegroup Business Card</title>
<link rel="stylesheet" href="https://fonts.googleapis.com/css2?family=Open+Sans:wght@400;600&display=swap">
<style>
  :root {
    --page-bg: #e9e4dc;
    --card-white: #ffffff;
    --orange: #f9704a;
    --red: #ee2024;
    --brand-teal: #1aa596;
    --text-light: #ffffff;
  }
  * { margin: 0; padding: 0; box-sizing: border-box; }
  html, body {
    width: 1200px;
    height: 960px;
    overflow: hidden;
    background: var(--page-bg);
  }
  .canvas {
    position: relative;
    width: 1200px;
    height: 960px;
  }
  .business-card {
    position: absolute;
    left: 150px;
    top: 223px;
    width: 900px;
    height: 514px;
    overflow: hidden;
    box-shadow: 0 6px 18px rgba(0, 0, 0, 0.25);
    font-family: "Open Sans", Arial, sans-serif;
  }
  .card-art {
    position: absolute;
    inset: 0;
    width: 100%;
    height: 100%;
  }
  .brand {
    position: absolute;
    left: 40px;
    top: 170px;
    width: 290px;
    text-align: center;
  }
  .brand-dot {
    display: block;
    width: 74px;
    height: 74px;
    margin: 0 auto 16px;
    border-radius: 50%;
    background: var(--brand-teal);
  }
  .brand-name {
    font-size: 30px;
    font-weight: 400;
    color: var(--brand-teal);
    letter-spacing: 0.5px;
  }
  .contact {
    position: absolute;
    right: 58px;
    color: var(--text-light);
    text-align: right;
  }
  .contact-name {
    top: 176px;
    font-size: 34px;
    font-weight: 600;
    line-height: 1;
  }
  .contact-role {
    top: 222px;
    font-size: 28px;
    font-weight: 400;
    line-height: 1;
  }
  .contact-phone {
    top: 282px;
    font-size: 36px;
    font-weight: 400;
    line-height: 1;
    display: flex;
    align-items: center;
    gap: 14px;
  }
  .phone-icon { width: 32px; height: 32px; }
  .contact-web {
    top: 410px;
    font-size: 26px;
    font-weight: 400;
    line-height: 1;
  }
</style>
</head>
<body>
<main class="canvas">
  <section class="business-card">
    <svg class="card-art" viewBox="0 0 900 514" aria-hidden="true">
      <defs>
        <linearGradient id="cardGradient" x1="0" y1="0" x2="1" y2="0">
          <stop offset="0.2" stop-color="#fa7650"/>
          <stop offset="1" stop-color="#ee2024"/>
        </linearGradient>
      </defs>
      <rect width="900" height="514" fill="url(#cardGradient)"/>
      <path d="M0,0 L230,0 C420,120 430,360 135,514 L0,514 Z" fill="#ffffff"/>
      <g fill="none" stroke="#ffffff" stroke-width="2">
        <path d="M250,0 C470,130 470,370 190,514"/>
        <path d="M275,0 C480,140 480,360 225,514"/>
        <path d="M300,0 C500,150 490,360 260,514"/>
        <path d="M330,0 C520,170 500,350 290,514"/>
      </g>
    </svg>

    <div class="brand">
      <span class="brand-dot"></span>
      <span class="brand-name">mapleridge group</span>
    </div>

    <p class="contact contact-name">Gareth Pembroke</p>
    <p class="contact contact-role">Director</p>
    <p class="contact contact-phone">
      <svg class="phone-icon" viewBox="0 0 32 32" aria-hidden="true">
        <path d="M3,11 C3,5 29,5 29,11 L29,13 L22,13 L22,10 L10,10 L10,13 L3,13 Z" fill="#ffffff"/>
        <path d="M9,14 L23,14 L27,28 L5,28 Z" fill="#ffffff"/>
        <g fill="#f4503a">
          <rect x="11" y="17" width="3" height="2"/><rect x="15" y="17" width="3" height="2"/><rect x="19" y="17" width="3" height="2"/>
          <rect x="10" y="21" width="3" height="2"/><rect x="15" y="21" width="3" height="2"/><rect x="20" y="21" width="3" height="2"/>
          <rect x="9" y="25" width="3" height="2"/><rect x="15" y="25" width="3" height="2"/><rect x="21" y="25" width="3" height="2"/>
        </g>
      </svg>
      <span>0452 803716</span>
    </p>
    <p class="contact contact-web">www.mapleridgegroup.com.au</p>
  </section>
</main>
</body>
</html>
```